Bussines Card - TR EDIFICACIONES, S.A.

We need a design for a business card.
I want it to look professional, but not old fashion.
We are like "young people', somehow i want it to look fresh, new, different, but still serious and professional.
I could use, a non typical design. (I mean, not just rectangular design).

The company Name is " TR EDIFICACIONES, S.A. " we are Panamenian company (spanish language) dedicated to construction and civil engeniering.

The company logo is attached, i use it with white background. Im not sure trying different one, could try.

Industry/Entity Type

Business

```html
<!DOCTYPE html>
<html lang="es">
<head>
<meta charset="utf-8">
<title>TR Edificaciones – Tarjeta de presentación</title>
<link href="https://fonts.googleapis.com/css2?family=Lato:wght@400;700;900&display=swap" rel="stylesheet">
<style>
  :root {
    --bg: #a9aaac;
    --card-front: #ffffff;
    --card-back: #3a3839;
    --back-tile: #444243;
    --ink-dark: #3d3d3d;
    --ink-mid: #4a4a4a;
    --ink-soft: #6b6b6b;
    --deco-grey: #d9d9d9;
    --white: #ffffff;
  }
  * { box-sizing: border-box; margin: 0; padding: 0; }
  html, body {
    width: 1200px; height: 900px; overflow: hidden;
    background: var(--bg);
    font-family: "Lato", Arial, sans-serif;
  }
  .stage { position: relative; width: 1200px; height: 900px; }

  .card {
    position: absolute;
    left: 330px;
    width: 540px; height: 315px;
    border-radius: 34px;
    overflow: hidden;
    box-shadow: 0 6px 18px rgba(0,0,0,.22);
  }

  /* Back */
  .card-back { top: 120px; background: var(--card-back); }
  .back-pattern {
    position: absolute; inset: 0;
    background: linear-gradient(135deg, var(--back-tile), var(--card-back));
  }
  .back-brand {
    position: absolute; right: 34px; bottom: 40px;
    display: flex; align-items: center; gap: 8px;
    color: var(--white); font-weight: 900; font-size: 13px; letter-spacing: 2px;
  }
  .back-brand .brand-square { width: 14px; height: 14px; background: var(--white); }

  /* Front */
  .card-front { top: 470px; background: var(--card-front); }
  .deco-block {
    position: absolute; left: 0; bottom: 0;
    width: 175px; height: 140px;
    background: var(--deco-grey);
  }
  .brand {
    position: absolute; right: 32px; top: 36px;
    display: flex; align-items: center; gap: 9px;
    color: var(--ink-dark); font-weight: 900; font-size: 16px; letter-spacing: 2.2px;
  }
  .brand-square { width: 16px; height: 16px; background: var(--ink-dark); }

  .person { position: absolute; left: 40px; top: 152px; }
  .person-name { font-size: 19px; font-weight: 700; color: var(--ink-dark); }
  .person-role { font-size: 13px; color: var(--ink-soft); margin-top: 2px; }

  .contact {
    position: absolute; right: 32px; top: 82px;
    list-style: none; text-align: right;
    font-size: 12.5px; color: var(--ink-mid); line-height: 17px;
  }
  .contact li { display: flex; justify-content: flex-end; align-items: flex-start; gap: 6px; }
  .contact .gap { margin-top: 10px; }
  .contact .web { font-weight: 700; color: var(--ink-dark); }
  .contact svg { width: 11px; height: 11px; margin-top: 3px; flex: none; fill: var(--ink-dark); }
  .contact .no-icon { padding-right: 17px; }
</style>
</head>
<body>
<main class="stage">

  <section class="card card-back" aria-label="Reverso de la tarjeta">
    <div class="back-pattern" role="img" aria-label="Patrón repetido de la marca en tonos gris oscuro"></div>
    <div class="back-brand"><span class="brand-square"></span>TR EDIFICACIONES</div>
  </section>

  <section class="card card-front" aria-label="Anverso de la tarjeta">
    <div class="deco-block"></div>

    <div class="brand"><span class="brand-square"></span>TR EDIFICACIONES</div>

    <ul class="contact">
      <li>Calle 48, Bella Vista
        <svg viewBox="0 0 12 12"><path d="M6 0a4 4 0 0 0-4 4c0 3 4 8 4 8s4-5 4-8a4 4 0 0 0-4-4zm0 5.6A1.6 1.6 0 1 1 6 2.4a1.6 1.6 0 0 1 0 3.2z"/></svg>
      </li>
      <li class="no-icon">Plaza Norte, 2do Piso Local 4</li>
      <li class="gap">555.210.348
        <svg viewBox="0 0 12 12"><rect x="3" y="0" width="6" height="12" rx="1.3"/><rect x="4.2" y="1.5" width="3.6" height="7" fill="#fff"/></svg>
      </li>
      <li>555.210.349
        <svg viewBox="0 0 12 12"><rect x="2" y="0" width="8" height="4"/><rect x="0" y="4" width="12" height="5" rx="1"/><rect x="2" y="8" width="8" height="4"/></svg>
      </li>
      <li>TRedificaciones.com
        <svg viewBox="0 0 12 12"><rect x="0" y="2" width="12" height="8" rx="1"/><path d="M0.5 2.5 6 7l5.5-4.5" stroke="#fff" stroke-width="1.2" fill="none"/></svg>
      </li>
      <li>info@TRedificaciones.com
        <svg viewBox="0 0 12 12"><circle cx="6" cy="6" r="5.5"/><path d="M0.5 6h11M6 .5c-3 3-3 8 0 11M6 .5c3 3 3 8 0 11" stroke="#fff" stroke-width=".9" fill="none"/></svg>
      </li>
      <li class="no-icon web">www.TRedificaciones.com</li>
    </ul>

    <div class="person">
      <p class="person-name">Marco Villalba</p>
      <p class="person-role">Engenier</p>
    </div>
  </section>

</main>
</body>
</html>
```